Design for Torvel Ginger Chewy Candy!

Hello! We are Torvel Enterprises Corp, a food manufacturer and distributor based in Los Angeles, CA. We manufacture Chips, Cookies, Juices, Dairy, and last but not least, Candies! We are launching our Ginger Chewy Candy soon and we need a great design for it!

Our Ginger Chewy Candy is a perfect mixture between sweet and spicy from the ginger itself. Torvel Ginger Chewy Candy a good relief for sore throat and nausea.

Now, other than a great design, we also welcome brand suggestions for the candy.
If you can come up with a logo for the Ginger Candy, that would be swell!

We are open to unique and out of the box design. We chose a few color schemes for the design, but feel free to step out of the box if you feel it suits the brand.

We don't have the exact size for the plastic pouch, but it should be a generic small plastic pouch size (approximately 4 oz resealable plastic pouch)

Please have fun designing the project, we can't wait to see all the great designs!

Cheers!

Target Market(s)

USA and Asian market
Age 30-70
Male and Female

Industry/Entity Type

Manufacture

Font styles to use
Serif
Sans Serif
Decorative

Colors
fff3d1
fee18a
fece3e
fbc994
fce8d3

Requirements
Must have
• Torvel Logo
• A picture of ginger (illustrations or photographs are welcome)
Nice to have
• Coating suggestions like Matte surface or SPOT UV
• Give us ideas of what the name of the chewy candy should be. Product name ideas are welcome!

```html
<!DOCTYPE html>
<html lang="en">
<head>
<meta charset="UTF-8">
<title>Torvel Spicora Pouch</title>
<link href="https://fonts.googleapis.com/css2?family=Montserrat:wght@600&family=Great+Vibes&family=Arimo:wght@400;700&display=swap" rel="stylesheet">
<style>
  :root {
    --stage: #d9d9db;
    --pouch-cream: #f3ecd5;
    --pouch-yellow: #f4f200;
    --brand-blue: #1b3aa8;
    --script-blue: #1540c8;
    --count-blue: #0d1ea0;
    --count-tan: #e6c99e;
    --tagline-grey: #d4d4b8;
    --ginger-light: #e6d2a0;
    --ginger-dark: #b89458;
    --seam-white: #ffffff;
    --zip-line: #e4dcc2;
  }
  * { margin: 0; padding: 0; box-sizing: border-box; }
  html, body { width: 1200px; height: 1000px; overflow: hidden; }
  body { background: var(--stage); position: relative; }

  .pouch {
    position: absolute;
    left: 330px; top: 40px;
    width: 540px; height: 920px;
    background: var(--pouch-cream);
    border-radius: 10px;
    overflow: hidden;
  }
  .pouch-shapes { position: absolute; inset: 0; }

  .brand-name {
    position: absolute;
    left: 150px; top: 62px; width: 240px;
    text-align: center;
    font-family: "Montserrat", sans-serif;
    font-weight: 600;
    font-size: 58px;
    line-height: 1.2;
    color: var(--brand-blue);
    letter-spacing: -1px;
  }

  .ginger-photo {
    position: absolute;
    left: 60px; top: 360px;
    width: 400px; height: 200px;
    border-radius: 45% 55% 40% 50% / 50% 45% 55% 50%;
    background: radial-gradient(ellipse at 45% 40%, var(--ginger-light), var(--ginger-dark));
  }

  .product-name {
    position: absolute;
    left: 20px; top: 570px; width: 500px;
    text-align: center;
    font-family: "Great Vibes", cursive;
    font-size: 124px;
    line-height: 1;
    color: var(--script-blue);
  }
  .tagline {
    position: absolute;
    left: 180px; top: 718px;
    font-family: "Arimo", sans-serif;
    font-size: 15px;
    color: var(--tagline-grey);
    white-space: nowrap;
  }

  .piece-count {
    position: absolute;
    left: 160px; top: 815px;
    width: 196px; height: 62px;
    background: var(--count-tan);
    display: flex; align-items: center; justify-content: center;
    font-family: "Arimo", sans-serif;
    font-weight: 700;
    font-size: 44px;
    color: var(--count-blue);
  }
</style>
</head>
<body>
  <div class="pouch">
    <svg class="pouch-shapes" width="540" height="920" viewBox="0 0 540 920" aria-hidden="true">
      <line class="zip-line" x1="0" y1="118" x2="540" y2="118" stroke="var(--zip-line)" stroke-width="2"/>
      <path class="lower-band-seam" d="M0 462 Q270 420 540 372" stroke="var(--seam-white)" stroke-width="10" fill="none"/>
      <path class="lower-band" d="M0 468 Q270 426 540 378 L540 920 L0 920 Z" fill="var(--pouch-yellow)"/>
      <path class="logo-tab" d="M150 0 L390 0 L390 160 L270 200 L150 160 Z" fill="var(--pouch-yellow)"/>
    </svg>

    <div class="brand-name">Torvel</div>

    <div class="ginger-photo" role="img" aria-label="Photograph of fresh ginger roots"></div>

    <div class="product-name">Spicora</div>
    <div class="tagline">a good relief for sore throat and nausea</div>

    <div class="piece-count">30 Pcs</div>
  </div>
</body>
</html>
```